Independent Statistical Consultant Business Card

I will be going out as an independent statistical consultant and need a business card. I specialize in data analysis and statistics for health care and public health

I am an Licensed Numeric Examiner from the Coastal Metrics Society. Would like to incorporate that logo into the design

The design should be modern with classic colors, convey accuracy, analytic creativity and responsiveness to client needs.

The name of the firm will be simply Tim Halvarsen Numeric Insight Services

To all designers, I want to clarify that the DCred logo and the phrase Licensed Numeric Examiner are not the name of the company nor the focus of the card. They are equivalent to being a Veltrano Qualified Engineer (VQE) but in the area of statistics The name of the firm will be: Tim Halvarsen, Numeric Insight Services. I look forward to your submissions. Thanks. Tim

```html
<!DOCTYPE html>
<html lang="en">
<head>
<meta charset="utf-8">
<title>Tim Halvarsen – Numeric Insight Services</title>
<link rel="stylesheet" href="https://fonts.googleapis.com/css2?family=Cabin:wght@400&family=Tinos&display=swap">
<style>
  :root {
    --paper: #ffffff;
    --slate: #434f58;
    --slate-deep: #3a454e;
    --ink: #1e1e1e;
    --signal-blue: #1440f5;
  }
  html, body {
    margin: 0;
    padding: 0;
    overflow: hidden;
    background: var(--paper);
  }
  .card {
    position: relative;
    width: 1200px;
    height: 762px;
    background: var(--paper);
    overflow: hidden;
    font-family: "Cabin", "Gill Sans", sans-serif;
  }
  .brand-mark-area {
    position: absolute;
    left: 100px;
    top: 307px;
    width: 320px;
    height: 320px;
    background: linear-gradient(160deg, var(--slate) 0%, var(--slate-deep) 100%);
  }
  .credential {
    position: absolute;
    right: 178px;
    top: 300px;
    text-align: right;
  }
  .credential-name {
    margin: 0;
    font-size: 66px;
    line-height: 1;
    color: var(--ink);
  }
  .credential-title {
    margin: 26px 0 0;
    font-family: "Tinos", "Times New Roman", serif;
    font-size: 17px;
    line-height: 1;
    color: var(--ink);
  }
  .identity {
    position: absolute;
    right: 148px;
    top: 465px;
    text-align: right;
    color: var(--slate);
  }
  .person-name {
    margin: 0;
    font-size: 68px;
    font-weight: 400;
    line-height: 1;
    letter-spacing: 1px;
  }
  .firm-name {
    margin: 14px 0 0;
    font-size: 35px;
    line-height: 1;
  }
  .phone {
    margin: 14px 6px 0 0;
    font-size: 35px;
    line-height: 1;
  }
</style>
</head>
<body>
  <main class="card">
    <div class="brand-mark-area" role="img" aria-label="Firm logo mark: a line chart with data points on a slate square"></div>

    <div class="credential">
      <p class="credential-name">DCred</p>
      <p class="credential-title">Licensed Numeric Examiner</p>
    </div>

    <div class="identity">
      <h1 class="person-name">TIM HALVARSEN</h1>
      <p class="firm-name">Numeric Insight Services</p>
      <p class="phone">p 000 000 0000</p>
    </div>
  </main>
</body>
</html>
```